Corvell Brochure

We need a brochure design for our company Corvell Shutters & Blinds VIC Pty Ltd. which is based in Melbourne. We are in the retail industry selling window furnishings such as roller blinds and plantation shutters.
We would like to have the brochure with a smart design and use neat dark colours like black and grey to symbolise our professionalism (please see the concept of our logo design as a reference). The brochure size should be A4.
The front and back cover page need to include our logo, and the overleaf of the front cover page is the "about us" introduction. Opposite to that will be the first page where locates our catalogue (with product page noted), then followed by all the products. Each product forms one page with at least two pictures. Finally there will be a company information page included with a map location.
The attached files include our company logo and our brochure contents for all products. There are 14 pages (including two cover pages) altogether and please strictly comply with the content of each page. The selected pictures for the brochure are in the dropbox linked below as well.
https://www.filetrove-share.example/sh/qpwzrtmkehvna3/XKTmWpL_Qr7GvdnRfeJh2sYz4
Retail

```html
<!DOCTYPE html>
<html lang="en">
<head>
<meta charset="UTF-8">
<title>Corvell Brochure – Outdoor Blinds &amp; Awnings</title>
<link rel="stylesheet" href="https://fonts.googleapis.com/css2?family=Questrial&display=swap">
<style>
  :root {
    --canvas-bg: #d9d7d4;
    --page-top: #2c2c2c;
    --page-bottom: #1d1d1d;
    --band-dark: #1a1a1a;
    --band-tab: #3a3a3a;
    --band-line: #5a5a5a;
    --text-main: #e6e6e6;
    --text-body: #c9c9c9;
    --frame-white: #f4f4f4;
    --frame-line: #8a8a8a;
  }
  * { margin: 0; padding: 0; box-sizing: border-box; }
  html, body { width: 1200px; height: 921px; overflow: hidden; }
  body {
    background: var(--canvas-bg);
    position: relative;
    font-family: "Questrial", "Helvetica Neue", Arial, sans-serif;
    color: var(--text-main);
  }
  .page {
    position: absolute;
    top: 123px;
    width: 489px;
    height: 684px;
    background: linear-gradient(180deg, var(--page-top) 0%, var(--page-bottom) 100%);
    overflow: hidden;
  }
  .page--left { left: 107px; }
  .page--right { left: 607px; }

  .page-header { position: absolute; left: 0; top: 0; width: 489px; height: 70px; }
  .page-header svg { position: absolute; inset: 0; }
  .page-title {
    position: absolute;
    left: 60px;
    top: 36px;
    font-size: 15px;
    font-weight: 400;
    letter-spacing: 0.6px;
    color: var(--text-main);
  }
  .page--right .page-title { left: 75px; }

  .photo { position: absolute; }
  .photo--wall-frame {
    left: 0; top: 118px; width: 217px; height: 350px;
    background: var(--frame-white);
  }
  .photo--wall-frame .photo-fill {
    position: absolute; left: 0; top: 14px; width: 203px; height: 322px;
    border: 4px solid var(--page-bottom);
    border-left: none;
    background: linear-gradient(160deg, #dfe4e8 0%, #7a4a3a 35%, #5b3a30 65%, #3a3a38 100%);
  }
  .photo--patio {
    left: 0; top: 484px; width: 222px; height: 153px;
    border: 4px solid var(--frame-white);
    border-left: none;
    background: linear-gradient(180deg, #cfc8c0 0%, #6a4a3e 40%, #2e2a28 100%);
  }
  .photo--awning-house {
    left: 41px; top: 131px; width: 152px; height: 226px;
    border: 1px solid var(--frame-line);
    background: linear-gradient(180deg, #8fb4d8 0%, #6e7478 30%, #3a3b3c 60%, #8a8a86 100%);
  }
  .photo--awning-feature {
    left: 210px; top: 214px; width: 279px; height: 470px;
    background: linear-gradient(180deg, #f0f0f0 0%, #d2d2d2 30%, #a8a8a8 62%, #5b4d8c 86%, #4a2f8a 100%);
  }

  .frame-lines { position: absolute; left: 0; top: 0; width: 489px; height: 684px; pointer-events: none; }

  .copy {
    position: absolute;
    font-size: 12px;
    line-height: 16px;
    letter-spacing: 0.2px;
    color: var(--text-body);
  }
  .copy strong { font-weight: 400; font-size: 17px; color: var(--text-main); }
  .copy--blinds { left: 240px; top: 262px; width: 242px; }
  .copy--awnings { left: 218px; top: 128px; width: 260px; }

  .spec { position: absolute; left: 6px; width: 198px; text-align: center; }
  .spec h2 { font-weight: 400; font-size: 17px; color: var(--text-main); line-height: 20px; }
  .spec ul { list-style: none; font-size: 12px; line-height: 16px; color: var(--text-body); }
  .spec ul li::before { content: "\2022\00a0"; }
  .spec--type { top: 451px; }
  .spec--size { top: 523px; }
</style>
</head>
<body>

<section class="page page--left">
  <header class="page-header">
    <svg viewBox="0 0 489 70" aria-hidden="true">
      <rect width="489" height="70" fill="var(--band-dark)"/>
      <polygon points="20,14 489,14 489,64 330,64 318,56 70,56" fill="var(--band-tab)" opacity="0.55"/>
      <polygon points="40,22 220,22 238,56 58,56" fill="var(--band-tab)"/>
      <line x1="0" y1="64" x2="489" y2="64" stroke="var(--band-line)" stroke-width="1"/>
    </svg>
    <h1 class="page-title">OUTDOOR BLINDS</h1>
  </header>

  <div class="photo photo--wall-frame">
    <div class="photo-fill" role="img" aria-label="Brick house wall with dark outdoor blinds lowered over the windows beside a paved path"></div>
  </div>
  <div class="photo photo--patio" role="img" aria-label="Covered outdoor entertaining area enclosed by dark outdoor blinds"></div>

  <p class="copy copy--blinds"><strong>Outdoor Blinds</strong> are a functional and stylish addition to your home's exterior. If you are one of those people who spend a lot of time at home and make use of outdoor rooms, you have to look for an effective way to enhance their overall condition. The best option that you have to consider is to install outdoor blinds to protect your decks, pool areas, balconies, patios and entertainment areas. With excellent outdoor blinds, you will be able to protect efficiently these areas from undesirable elements of nature.</p>
</section>

<section class="page page--right">
  <header class="page-header">
    <svg viewBox="0 0 489 70" aria-hidden="true">
      <rect width="489" height="70" fill="var(--band-dark)"/>
      <polygon points="20,14 489,14 489,64 330,64 318,56 70,56" fill="var(--band-tab)" opacity="0.55"/>
      <polygon points="40,22 180,22 198,56 58,56" fill="var(--band-tab)"/>
      <line x1="0" y1="64" x2="489" y2="64" stroke="var(--band-line)" stroke-width="1"/>
    </svg>
    <h1 class="page-title">AWNINGS</h1>
  </header>

  <div class="photo photo--awning-house" role="img" aria-label="Modern weatherboard house with a grey awning over a sunny deck with lounge chairs"></div>
  <svg class="frame-lines" viewBox="0 0 489 684" aria-hidden="true">
    <polyline points="27,108 113,108" fill="none" stroke="var(--frame-line)" stroke-width="1"/>
    <polyline points="27,108 27,210" fill="none" stroke="var(--frame-line)" stroke-width="1"/>
    <polyline points="120,381 204,381 204,300" fill="none" stroke="var(--frame-line)" stroke-width="1"/>
  </svg>

  <p class="copy copy--awnings"><strong>Awnings</strong> offer a stylish way to shelter your window, while they add value to your home. Awnings can also boost the curb appeal of your home aside from they perform various useful functions.</p>

  <div class="photo photo--awning-feature" role="img" aria-label="White house corner with grey folding arm awnings over the windows and purple pansies in the foreground"></div>

  <div class="spec spec--type">
    <h2>Awning Type</h2>
    <ul>
      <li>Standard</li>
      <li>Folding Arm</li>
    </ul>
  </div>
  <div class="spec spec--size">
    <h2>Blind Size Range</h2>
    <ul>
      <li>Width: 965 – 4865mm</li>
      <li>Drop: 900 – 3600mm</li>
      <li>Width: 3000 – 6000mm</li>
      <li>Drop: 1600 – 4000mm</li>
    </ul>
  </div>
</section>

</body>
</html>
```